Kessel Fahrwerkstatt
Sehr angenehme zusammenarbeit nicht aufdringlich und genau auf die Wünsche eingegangen. Wir werde sicher noch mehr zusammen Arbeiten. Gruss Lukas Hemmerle Inhaber Kessel Fahrwerkstatt
Zielgruppe
Dinks und Kunden mit viel Erfolg und hohem Ausgabepotential.
Aufgabenstellung
Unsere Firma vertreibt Fahrzeuge im Luxusbereich hauptgebiet Valtro aber auch andere Sportwagen. Was uns fehlt ist ein optischer Wiedererkennugswert. Deshalb hätten wir gerne ein Visitenkarten Design und Briefpapier Design. Später soll auch noch eine Webseite mit gleichem Wiedererkennungswert entstehen. " Roter Faden "

```html
<!DOCTYPE html>
<html lang="de">
<head>
<meta charset="utf-8">
<title>Kessel Fahrwerkstatt – Visitenkarte</title>
<link rel="stylesheet" href="https://fonts.googleapis.com/css2?family=Questrial&display=swap">
<style>
  :root {
    --stage: #e8e5e1;
    --card-front-dark: #a99b8b;
    --card-front-light: #ece1d0;
    --card-back: #ffffff;
    --ink: #1e1b18;
    --ink-soft: #3a3530;
    --accent: #b59f84;
    --mark: #6b5a47;
    --shadow: rgba(40, 32, 24, 0.28);
  }
  * { box-sizing: border-box; margin: 0; padding: 0; }
  html, body {
    width: 1200px; height: 839px; overflow: hidden;
    background: var(--stage);
    font-family: "Questrial", "Century Gothic", sans-serif;
    color: var(--ink);
  }
  .sheet {
    width: 1200px; height: 839px;
    display: flex; align-items: center; justify-content: center; gap: 60px;
  }
  .card {
    position: relative;
    width: 510px; height: 330px;
    overflow: hidden;
    box-shadow: 0 14px 34px var(--shadow);
  }

  /* Front */
  .card--front {
    background: radial-gradient(ellipse at 70% 25%, var(--card-front-light) 0%, #cdbfab 45%, var(--card-front-dark) 100%);
  }
  .brand-dot {
    position: absolute; left: 221px; top: 72px;
    width: 66px; height: 66px; border-radius: 50%;
    background: var(--mark);
  }
  .brand-name {
    position: absolute; left: 0; right: 0; top: 156px;
    text-align: center; font-weight: 400; color: var(--ink);
    line-height: 1.2;
  }
  .brand-name__main {
    display: block; font-size: 22px; letter-spacing: 6px; text-transform: uppercase;
  }
  .brand-name__sub {
    display: block; font-size: 22px; letter-spacing: 1px;
  }

  /* Back */
  .card--back { background: var(--card-back); }
  .vertical {
    position: absolute;
    writing-mode: vertical-rl;
    transform: rotate(180deg);
    white-space: nowrap;
  }
  .holder {
    left: 62px; top: 66px; bottom: 92px;
    display: flex; flex-direction: column; align-items: flex-start; gap: 3px;
  }
  .holder__name { font-size: 22px; letter-spacing: 1.5px; color: var(--accent); line-height: 1; }
  .holder__role { font-size: 10px; color: var(--accent); letter-spacing: 0.3px; line-height: 1; }
  .back-dot {
    position: absolute; left: 112px; top: 70px;
    width: 62px; height: 62px; border-radius: 50%;
    background: var(--mark);
  }
  .links {
    left: 206px; top: 44px; bottom: 34px;
    font-size: 10px; color: var(--ink); letter-spacing: 0.2px; line-height: 1;
  }
  .links__sep { margin: 7px 0; }
  .links__mail { color: var(--accent); }
  .addresses {
    position: absolute; left: 242px; top: 200px;
    font-size: 12px; line-height: 1.35;
  }
  .addresses dt { color: var(--accent); font-size: 11px; }
  .addresses dd { color: var(--ink-soft); margin-bottom: 10px; }
</style>
</head>
<body>
<main class="sheet">
  <section class="card card--front" aria-label="Visitenkarte Vorderseite">
    <span class="brand-dot" aria-hidden="true"></span>
    <h1 class="brand-name">
      <span class="brand-name__main">Kessel</span>
      <span class="brand-name__sub">Fahrwerkstatt</span>
    </h1>
  </section>

  <section class="card card--back" aria-label="Visitenkarte Rückseite">
    <div class="vertical holder">
      <span class="holder__name">Lukas Hemmerle</span>
      <span class="holder__role">[Geschäftsführung]</span>
    </div>
    <span class="back-dot" aria-hidden="true"></span>
    <p class="vertical links">
      <span>www.kessel-fahrwerk.ch</span><span class="links__sep">|</span><span class="links__mail">info@kessel-fahrwerk.ch</span>
    </p>
    <dl class="addresses">
      <dt>Büro:</dt>
      <dd>Mühlegasse 14 CH 8302 Kloten</dd>
      <dt>Showroom:</dt>
      <dd>Seestrasse 52 - CH 8712 Stäfa</dd>
    </dl>
  </section>
</main>
</body>
</html>
```